Face lift needed for client website www.vorthanmed.com

vorthanmed is Dallas based medical device company. 1. Would like to see a home page design that stays to the company colors (blue, gray, white, black). Home page is boring. Need lively pate with active people background who could benefit from the products. Compare with www.quelbrintex.com and www.parnivo.com. 2. Would like new looks for each of "Our Company" (i.e. our philosophy / our management team).

Industry/Entity Type

Medical

```html
<!DOCTYPE html>
<html lang="en">
<head>
<meta charset="utf-8">
<title>Vorthanmed — Our Philosophy</title>
<link href="https://fonts.googleapis.com/css2?family=Raleway:wght@300;400;500;600;700&display=swap" rel="stylesheet">
<style>
:root{
  --brand-blue:#1f6fb2;
  --band-blue:#2a6cae;
  --ink:#222;
  --body:#555;
  --card:#f2f2f2;
  --rule:#dedede;
  --white:#fff;
}
*{margin:0;padding:0;box-sizing:border-box}
html,body{width:732px;height:1200px;overflow:hidden}
body{position:relative;background:var(--white);font-family:'Raleway',sans-serif;color:var(--body)}
.abs{position:absolute}

/* header */
.site-header{left:0;top:0;width:732px;height:58px;background:var(--white);box-shadow:0 1px 3px rgba(0,0,0,.06);z-index:2}
.top-rule{left:38px;top:0;width:654px;height:3px;background:var(--brand-blue)}
.brand{display:flex;align-items:center;gap:5px;color:var(--brand-blue);font-weight:600;font-size:17px;letter-spacing:.3px}
.brand-dot{width:14px;height:14px;border-radius:50%;background:#8a8f96}
.site-header .brand{left:38px;top:18px}
.main-nav{left:384px;top:25px;display:flex;gap:14px;font-size:8px;font-weight:500;color:#333;letter-spacing:.2px}
.main-nav .active{color:var(--brand-blue);border-bottom:1px solid var(--brand-blue);padding-bottom:3px}
.search-icon{left:680px;top:24px}

/* hero */
.hero{left:0;top:58px;width:732px;height:121px;background:linear-gradient(90deg,#f1f1f0 0%,#ecebea 35%,#b9aea4 55%,#e9e7e4 68%,#c8b4a0 80%,#eeece9 100%)}
.hero-title{left:70px;top:105px;font-size:24px;font-weight:300;color:var(--brand-blue)}

/* philosophy */
.philosophy{left:68px;top:221px;width:290px;font-size:7.6px;line-height:14px}
.philosophy p{margin-bottom:14px}
.philosophy h3{font-size:13px;font-weight:400;color:#333;margin:-4px 0 12px}
.feature-image{left:412px;top:208px;width:279px;height:186px;background:radial-gradient(ellipse at 45% 40%,#3a7fe0 0%,#1846b8 40%,#050a25 80%,#000 100%)}
.feature-card{left:412px;top:394px;width:279px;height:186px;background:#f3f3f3;box-shadow:0 3px 3px -2px rgba(0,0,0,.1);padding:20px 27px}
.feature-card h2{font-size:17px;font-weight:400;color:var(--ink);margin-bottom:10px}
.feature-card p{font-size:7.6px;line-height:14px}

/* team */
.divider{left:38px;top:708px;width:654px;height:1px;background:var(--rule)}
.team-title{left:0;top:731px;width:732px;text-align:center;font-size:18px;font-weight:400;color:var(--ink)}
.team{left:38px;top:773px;display:flex;gap:21px}
.member{width:114px;height:152px;background:var(--card);box-shadow:0 3px 3px -2px rgba(0,0,0,.12);text-align:center;padding-top:17px}
.member-photo{width:67px;height:89px;margin:0 auto 9px;background:linear-gradient(180deg,#3f7fd6 0%,#1e56a8 55%,#1b2c4a 100%)}
.member h4{font-size:10px;font-weight:700;color:#111;line-height:12px}
.member span{font-size:7.5px;color:#222}

/* footer */
.footer-band{left:0;top:984px;width:732px;height:216px;background:var(--band-blue)}
.footer-corner{left:30px;top:976px;width:0;height:0;border-left:8px solid transparent;border-bottom:8px solid #1d4f82}
.footer-panel{left:38px;top:976px;width:355px;height:187px;background:#f1f1f1}
.footer-panel .brand{left:25px;top:30px}
.address{left:30px;top:63px;font-size:7.5px;line-height:10px;color:#333}
.social{left:30px;top:96px;display:flex;gap:4px}
.social i{display:block;width:16px;height:16px;border-radius:50%}
.footer-nav{left:228px;top:32px;list-style:none;font-size:7.6px;font-weight:600;line-height:12.8px;color:#222}
.footer-nav .active{color:var(--brand-blue)}
.map{left:393px;top:976px;width:299px;height:187px;background:linear-gradient(135deg,#ece8df 0%,#e6e2d8 50%,#ede9e1 100%)}
.map-bar{left:393px;top:976px;width:299px;height:34px;background:rgba(40,40,40,.85);color:var(--white);font-size:15px;font-weight:300;padding:6px 10px}
.legal{left:38px;top:1173px;font-size:7.8px;color:var(--white)}
.legal-links{left:594px;top:1173px;font-size:7.8px;color:var(--white);display:flex;gap:7px}
.legal-links b{font-weight:400;opacity:.5}
</style>
</head>
<body>

<header class="site-header abs">
  <div class="top-rule abs"></div>
  <div class="brand abs"><span class="brand-dot"></span>Vorthanmed</div>
  <nav class="main-nav abs">
    <span>HOME</span><span class="active">OUR COMPANY</span><span>PRODUCTS</span><span>NEWS ROOM</span><span>CONTACT US</span>
  </nav>
  <svg class="search-icon abs" width="11" height="11" viewBox="0 0 11 11"><circle cx="4.5" cy="4.5" r="3.5" fill="none" stroke="#1f6fb2" stroke-width="1.5"/><line x1="7" y1="7" x2="10" y2="10" stroke="#1f6fb2" stroke-width="1.6"/></svg>
</header>

<section class="hero abs" role="img" aria-label="Soft-focus photo of active people outdoors"></section>
<h1 class="hero-title abs">Our Philosophy</h1>

<article class="philosophy abs">
  <p>We, Vorthanmed, are a nimble and flexible company building our business on competence and relationships.</p>
  <p>We, Vorthanmed, are about healing people with spinal disorders.</p>
  <p>We strive to develop and distribute easy-to-use, quality products through close collaboration with end users and their facilities in order to deliver true value and care to all our clients.</p>
  <p>Lorem Ipsum is simply dummy text of the printing and typesetting industry. Lorem Ipsum has been the industry's standard dummy text ever since the 1500s, when an unknown printer took a galley of type and scrambled it to make a type specimen book. It has survived not only five centuries, but also the leap into electronic typesetting, remaining essentially unchanged. It was popularised in the 1960s with the release of Tessaline sheets containing Lorem Ipsum passages, and more recently with desktop publishing software like Quillset Pagemaster including versions of Lorem Ipsum</p>
  <h3>Subtitle One</h3>
  <p>Contrary to popular belief, Lorem Ipsum is not simply random text. It has roots in a piece of classical Latin literature from 45 BC, making it over 2000 years old. Edwin Marlowe, a Latin professor at Ashgrove College in Virginia, looked up one of the more obscure Latin words, consectetur, from a Lorem Ipsum passage, and going through the cites of the word in classical literature, discovered the undoubtable source. Lorem Ipsum comes from sections 1.10.32 and 1.10.33 of "de Finibus Bonorum et Malorum" (The Extremes of Good and Evil) by Lucan Vell, written in 45 BC. This book is a treatise on the theory of ethics, very popular during the Renaissance. The first line of Lorem Ipsum, "Lorem ipsum dolor sit amet..", comes from a line in section 1.10.32</p>
</article>

<div class="feature-image abs" role="img" aria-label="Illustration of a human skeleton and spine in blue"></div>
<div class="feature-card abs">
  <h2>Active For Life</h2>
  <p>Vorthanmed is a forward thinking medical device company that strives to develop products and services that treat spinal disorders. The Vorthanmed portfolio showcases a wide range of complementary products that include a minimally invasive spine system, posterior cervical system, thoracolumbar system, anterior cervical plate system, interbody device options, and biologic solutions.</p>
</div>

<div class="divider abs"></div>
<h2 class="team-title abs">Management Team</h2>
<div class="team abs">
  <div class="member"><div class="member-photo" role="img" aria-label="Portrait of Marcus Ellory"></div><h4>Marcus Ellory</h4><span>President &amp; CEO</span></div>
  <div class="member"><div class="member-photo" role="img" aria-label="Portrait of Petra Vanlowe"></div><h4>Petra Vanlowe</h4><span>Chief Financial Officer</span></div>
  <div class="member"><div class="member-photo" role="img" aria-label="Portrait of Rina Desmond"></div><h4>Rina Desmond</h4><span>General Cousel</span></div>
  <div class="member"><div class="member-photo" role="img" aria-label="Portrait of Theo Karsh"></div><h4>Theo Karsh</h4><span>VP of Operations &amp; R&amp;D</span></div>
  <div class="member"><div class="member-photo" role="img" aria-label="Portrait of Grant Holloway"></div><h4>Grant Holloway</h4><span>Regional Sales Director</span></div>
</div>

<footer>
  <div class="footer-band abs"></div>
  <div class="footer-corner abs"></div>
  <div class="footer-panel abs">
    <div class="brand abs"><span class="brand-dot"></span>Vorthanmed</div>
    <div class="address abs">2280 Calloway Parkway, Dallas, TX 75240<br>(800) 555-0172</div>
    <div class="social abs">
      <i style="background:#3b5998"></i><i style="background:#29a9e1"></i><i style="background:#dd4b39"></i><i style="background:#0e76a8"></i><i style="background:#1ab7ea"></i>
    </div>
    <ul class="footer-nav abs">
      <li class="active">HOME</li><li>OUR COMPANY</li><li>BLOG</li><li>PRODUCTS</li><li>NEWS ROOM</li><li>CONTACT US</li>
    </ul>
  </div>
  <div class="map abs" role="img" aria-label="Street map showing the office location"></div>
  <div class="map-bar abs">Locate Us</div>
  <div class="legal abs">© 2014, Vorthanmed - All Rights Reserved</div>
  <div class="legal-links abs"><span>Sitemap</span><b>|</b><span>Privacy Policy</span></div>
</footer>

</body>
</html>
```